Business Card Design

We are a commercial real estate brokerage in San Francisco, leasing office buildings downtown.
I would like a clean, elegant look. Simple but powerful .

Industry/Entity Type

Business

Contact Information for Business Card

Colin Farrow
lic# 07281549
415.555.0172
colin@tarvo-commercial.example
tarvo-commercial.example

```html
<!DOCTYPE html>
<html lang="en">
<head>
<meta charset="utf-8">
<title>Tarvo Commercial – Business Card</title>
<link href="https://fonts.googleapis.com/css2?family=Cinzel:wght@400;600&display=swap" rel="stylesheet">
<style>
  :root {
    --backdrop: #e9e7e4;
    --card-base: #222223;
    --card-band: #2b2b2c;
    --card-deep: #1a1a1b;
    --panel-light: #303032;
    --bar-black: #111112;
    --text-main: #ececec;
    --text-soft: #bdbdbd;
    --accent-blue: #9fb4d0;
  }
  * { margin: 0; padding: 0; box-sizing: border-box; }
  html, body {
    width: 1200px; height: 899px; overflow: hidden;
    background: var(--backdrop);
    font-family: "Cinzel", Georgia, serif;
  }
  .stage {
    position: relative; width: 1200px; height: 899px;
    display: flex; align-items: center; justify-content: center; gap: 40px;
  }
  .card {
    position: relative; width: 540px; height: 309px;
    background: var(--card-base); overflow: hidden;
    box-shadow: 0 10px 24px rgba(0,0,0,0.25);
  }

  /* Brand lockup: square plus two-line name, one size, one colour */
  .brand {
    position: absolute; display: flex; align-items: center;
    color: var(--accent-blue); font-weight: 600; letter-spacing: 0.05em;
    text-transform: uppercase; white-space: nowrap; line-height: 1.08;
  }
  .brand__mark { background: var(--accent-blue); flex: none; }
  .brand__name { display: flex; flex-direction: column; }

  /* Front */
  .front__band-left {
    position: absolute; left: 0; top: 0; width: 120px; height: 100%;
    background: var(--card-band);
  }
  .front__band-right {
    position: absolute; right: 0; top: 0; width: 110px; height: 100%;
    background: var(--card-band);
  }
  .front .brand {
    left: 120px; width: 310px; top: 50%; transform: translateY(-50%);
    justify-content: center; font-size: 24px; gap: 14px;
  }
  .front .brand__mark { width: 40px; height: 40px; }

  /* Back */
  .back__column {
    position: absolute; left: 0; top: 0; width: 160px; height: 100%;
    background: var(--card-deep);
  }
  .back__logo-block {
    position: absolute; left: 0; top: 0; width: 160px; height: 84px;
    background: var(--panel-light);
  }
  .back .brand {
    left: 0; width: 160px; top: 42px; transform: translateY(-50%);
    justify-content: center; font-size: 11px; gap: 8px;
  }
  .back .brand__mark { width: 18px; height: 18px; }

  .contact { position: absolute; left: 196px; top: 42px; right: 0; color: var(--text-main); }
  .contact__name {
    font-size: 34px; font-weight: 400; letter-spacing: 0.02em; text-transform: uppercase;
    display: flex; align-items: flex-end; gap: 12px; white-space: nowrap;
  }
  .contact__name-bar { flex: 1; height: 16px; background: var(--bar-black); margin-bottom: 6px; }
  .contact__lic { font-size: 14px; color: var(--text-soft); margin-top: 2px; text-transform: uppercase; }
  .contact__phone { font-size: 22px; margin-top: 30px; letter-spacing: 0.04em; }
  .contact__email {
    display: inline-block; margin-top: 4px; font-size: 14px; text-transform: uppercase;
    background: var(--bar-black); padding: 2px 8px 2px 6px; letter-spacing: 0.03em;
    white-space: nowrap;
  }
  .contact__web {
    position: absolute; left: 160px; right: 0; bottom: 40px; height: 22px;
    background: var(--bar-black); color: var(--text-soft);
    font-size: 12px; letter-spacing: 0.06em; text-transform: uppercase;
    display: flex; align-items: center; justify-content: flex-end; padding-right: 20px;
    white-space: nowrap;
  }
</style>
</head>
<body>
  <main class="stage">
    <section class="card front" aria-label="Card front">
      <div class="front__band-left"></div>
      <div class="front__band-right"></div>
      <div class="brand">
        <span class="brand__mark"></span>
        <span class="brand__name"><span>Tarvo</span><span>Commercial</span></span>
      </div>
    </section>

    <section class="card back" aria-label="Card back">
      <div class="back__column"></div>
      <div class="back__logo-block"></div>
      <div class="brand">
        <span class="brand__mark"></span>
        <span class="brand__name"><span>Tarvo</span><span>Commercial</span></span>
      </div>
      <div class="contact">
        <h1 class="contact__name">Colin Farrow<span class="contact__name-bar"></span></h1>
        <p class="contact__lic">Lic# 07281549</p>
        <p class="contact__phone">415.555.0172</p>
        <p class="contact__email">colin@tarvo-commercial.example</p>
      </div>
      <p class="contact__web">www.tarvo-commercial.example</p>
    </section>
  </main>
</body>
</html>
```